Stationery for a professional investment company

Hi, I would like to design full stationary set based on my logo. I would like to use the red color in the file as well as white.

The design should be simple, credible and serious.

Orvane manages portfolio companies. The companies that represent our industry are

LMW (https://www.lmw-example.com)

HVN Capital

Target Market(s)

Investment professionals

Industry/Entity Type

Investment Advisory

Font styles to use
Sans Serif

Colors
ec1f27

Requirements
Must have
• A4 Letterhead, C4 envelop, C5 envelop, DL envelop

```html
<!DOCTYPE html>
<html lang="en">
<head>
<meta charset="utf-8">
<title>Orvane Capital Letterhead</title>
<link rel="stylesheet" href="https://fonts.googleapis.com/css2?family=Lato:ital,wght@0,300;0,400;0,700;1,700&family=Tinos&display=swap">
<style>
  :root {
    --brand-red: #85141f;
    --backdrop: #c4c4c4;
    --paper: #ffffff;
    --ink: #3e3e3e;
    --ink-dark: #1a1a1a;
    --ink-muted: #777777;
  }
  * { box-sizing: border-box; margin: 0; padding: 0; }
  html, body {
    width: 1082px; height: 1200px; overflow: hidden;
    background: var(--backdrop);
  }
  .letterhead {
    position: absolute; left: 159px; top: 73px;
    width: 765px; height: 1061px;
    background: var(--paper);
    font-family: "Lato", sans-serif;
    color: var(--ink);
  }
  .brand-name {
    position: absolute; left: 69px; top: 60px;
    font-family: "Lato", sans-serif; font-weight: 700;
    font-size: 46px; line-height: 1; letter-spacing: 0;
    color: var(--brand-red);
  }
  .contact-list {
    position: absolute; left: 606px; top: 37px; height: 68px;
    border-left: 1px solid var(--brand-red);
    padding-left: 8px; list-style: none;
    font-family: "Tinos", serif; font-size: 8.5px; color: var(--ink-dark);
  }
  .contact-list li {
    display: flex; align-items: center; gap: 4px;
    height: 16.3px; margin-top: 1px;
  }
  .contact-list svg { width: 9px; height: 9px; flex: none; }
  .recipient { position: absolute; left: 63px; top: 263px; letter-spacing: 0.5px; }
  .recipient-label { font-size: 14px; color: var(--ink-dark); margin-bottom: 17px; }
  .recipient-name { font-size: 15px; color: var(--brand-red); line-height: 15px; }
  .recipient-role { font-size: 10px; color: var(--ink-muted); line-height: 11px; }
  .recipient-detail { font-size: 14.5px; color: var(--ink-dark); line-height: 17.3px; }
  .letter-body {
    position: absolute; left: 63px; top: 396px; width: 645px;
    font-weight: 300; font-size: 15.6px; line-height: 17.2px;
    letter-spacing: 0.5px; color: var(--ink);
  }
  .letter-body p { margin-bottom: 17.2px; }
  .letter-body p.extra-gap { margin-top: 17px; }
  .sign-off {
    position: absolute; left: 63px; top: 810px;
    font-weight: 700; font-style: italic; font-size: 14px; color: var(--ink-dark);
  }
  .signature {
    position: absolute; left: 63px; top: 836px; width: 90px; height: 26px;
    background: linear-gradient(90deg, #d9d9d9, #eeeeee);
  }
  .footer-band {
    position: absolute; left: 0; top: 1038px; width: 765px; height: 23px;
    background: var(--brand-red);
  }
  .footer-mark {
    position: absolute; left: 638px; top: 3px;
    font-weight: 700; font-size: 15px; line-height: 17px; color: var(--paper);
  }
</style>
</head>
<body>
<main class="letterhead">
  <div class="brand-name">ORVANE CAPITAL</div>

  <ul class="contact-list">
    <li>
      <svg viewBox="0 0 10 10"><circle cx="5" cy="5" r="4.3" fill="none" stroke="var(--brand-red)" stroke-width="1"/><path d="M3.3 2.8l1 1-.5.7c.4.7.9 1.2 1.6 1.6l.7-.5 1 1-.7.8C4.9 7.3 2.7 5.1 2.5 3.5z" fill="var(--brand-red)"/></svg>
      (02) 5550 4187
    </li>
    <li>
      <svg viewBox="0 0 10 10"><rect x="3" y="1" width="4" height="2.5" fill="var(--brand-red)"/><rect x="1" y="3.5" width="8" height="3.5" rx="0.6" fill="var(--brand-red)"/><rect x="3" y="6" width="4" height="3" fill="var(--brand-red)"/></svg>
      (02) 5550 4188
    </li>
    <li>
      <svg viewBox="0 0 10 10"><rect x="1" y="2" width="8" height="6" fill="none" stroke="var(--brand-red)" stroke-width="0.9"/><path d="M1 2l4 3.3L9 2M1 8l3-2.6M9 8L6 5.4" fill="none" stroke="var(--brand-red)" stroke-width="0.9"/></svg>
      info@northlane-advisory.com
    </li>
    <li>
      <svg viewBox="0 0 10 10"><circle cx="5" cy="5" r="4" fill="var(--brand-red)"/><path d="M1 5h8M5 1v8M2 3h6M2 7h6" stroke="#fff" stroke-width="0.6"/></svg>
      ww.northlane-advisory.com
    </li>
  </ul>

  <section class="recipient">
    <p class="recipient-label">TO</p>
    <p class="recipient-name">HARPER</p>
    <p class="recipient-role">Director</p>
    <p class="recipient-detail">Design Studio</p>
    <p class="recipient-detail">A: 555 010 274</p>
    <p class="recipient-detail">B:5550&nbsp; 199 362</p>
  </section>

  <section class="letter-body">
    <p>Lorem ipsum dolor sit amet, consectetur adipiscing elit. Vestibulum consectetur egestas metus, quis scelerisque tortor consectetur sed. Nullam sit amet lorem sed arcu faucibus semper. Vestibulum ante ipsum primis in faucibus orci luctus et ultrices posuere cubilia Curae; Sed sagittis arcu ut ligula molestie malesuada. Suspendisse posuere tincidunt elit, at ullamcorper augue blandit vitae.</p>
    <p>Cras egestas vestibulum pulvinar. Donec iaculis imperdiet hendrerit. Sed mollis, enim quis hendrerit dictum, tortor mauris vulputate ligula, viverra porta magna libero at mi. Integer odio nisl, luctus nec dui in, rutrum sollicitudin nisi. Suspendisse nec erat eros.</p>
    <p>Sed dictum quam arcu, sit amet ullamcorper orci faucibus eget. Morbi finibus ante at risus commodo, nec ullamcorper nulla tincidunt. Integer eu molestie nulla, sed consequat tortor. Sed ullamcorper congue metus, vitae dictum nibh luctus sed. Suspendisse ornare purus fermentum, viverra elit sed, bibendum ex. Vivamus semper diam vel diam laoreet rutrum. Ut porta fermentum velit. Vestibulum vitae semper nisl. Sed facilisis at ex et vestibulum. Donec at magna ut eros pulvinar hendrerit.</p>
    <p class="extra-gap">Sed dictum quam arcu, sit amet ullamcorper orci faucibus eget. Morbi finibus ante at risus commodo, nec ullamcorper nulla tincidunt. Integer eu molestie nulla, sed consequat tortor. Sed ullamcorper congue metus, vitae dictum nibh luctus sed. Suspendisse ornare purus fermentum, viverra elit sed, bibendum ex.</p>
  </section>

  <p class="sign-off">Regards,</p>
  <div class="signature" role="img" aria-label="Handwritten signature of the sender"></div>

  <footer class="footer-band">
    <span class="footer-mark">ORVANE</span>
  </footer>
</main>
</body>
</html>
```